we need a business card. We are an online company that provides work life balance services to our members. our website can be viewed at www.quillmoorhub.com.au
Our company logo is attached as well as a business card look that i like.

```html
<!DOCTYPE html>
<html lang="en">
<head>
<meta charset="utf-8">
<title>Quillmoor Hub – Business Card</title>
<link href="https://fonts.googleapis.com/css2?family=Open+Sans:ital,wght@0,400;0,600;0,700;0,800;1,600;1,700&display=swap" rel="stylesheet">
<style>
  :root{
    --bg:#e6e7e8;
    --card:#ffffff;
    --green:#8cc63f;
    --green-light:#a8cf45;
    --green-dark:#2e9448;
    --grey:#c8c9cb;
    --logo-grey:#bdbec0;
    --ink:#333333;
  }
  *{box-sizing:border-box;margin:0;padding:0}
  html,body{width:1200px;height:1078px;overflow:hidden;background:var(--bg);
    font-family:"Open Sans",Arial,sans-serif;color:var(--ink)}
  .card{position:absolute;left:197px;width:805px;height:460px;background:var(--card);
    box-shadow:0 6px 18px rgba(0,0,0,.18);overflow:hidden}
  .card--front{top:53px}
  .card--back{top:565px}

  .brand{position:absolute;display:flex;align-items:center;gap:16px}
  .brand__dot{width:64px;height:64px;border-radius:50%;background:var(--green)}
  .brand__name{font-size:56px;font-weight:400;color:var(--logo-grey);letter-spacing:-1px}

  /* front */
  .card--front .brand{left:60px;top:70px}
  .front-band{position:absolute;left:0;top:270px;width:100%;height:130px;background:var(--green)}
  .front-blocks{position:absolute;left:0;top:270px;width:110px;height:130px;display:flex;flex-direction:column}
  .front-blocks span{flex:1}
  .role-block{position:absolute;right:50px;top:284px;text-align:right;color:#fff}
  .role-block__title{font-size:46px;font-weight:800;letter-spacing:1px;line-height:1.1}
  .role-block__name{font-size:30px;font-weight:700;line-height:1.2}

  /* back */
  .contact{position:absolute;left:50px;top:40px;font-size:19px;line-height:1.3}
  .heading{font-weight:700;font-style:italic;text-transform:uppercase;font-size:19px;letter-spacing:.5px}
  .card--back .brand{left:50px;top:168px}
  .card--back .brand__dot{width:54px;height:54px}
  .card--back .brand__name{font-size:46px}
  .social{position:absolute;right:50px;top:120px;font-size:19px;line-height:1.3;text-align:left}
  .person{position:absolute;right:50px;top:296px;text-align:right}
  .person__name{font-size:30px;font-weight:700;color:var(--green-dark);text-transform:uppercase}
  .person__role{font-size:19px;font-weight:400;text-transform:uppercase}
  .back-stripe{position:absolute;left:0;bottom:30px;width:100%;height:26px;background:var(--green)}
  .back-blocks{position:absolute;left:0;bottom:56px;display:flex;height:30px}
  .back-blocks span{width:50px}
  .c-light{background:var(--green-light)}
  .c-grey{background:var(--grey)}
  .c-dark{background:var(--green-dark)}
  .c-green{background:var(--green)}
</style>
</head>
<body>
  <section class="card card--front">
    <div class="brand"><span class="brand__dot"></span><span class="brand__name">quillmoorhub</span></div>
    <div class="front-band"></div>
    <div class="front-blocks"><span class="c-grey"></span><span class="c-light"></span><span class="c-grey"></span><span class="c-dark"></span></div>
    <div class="role-block">
      <div class="role-block__title">FOUNDER</div>
      <div class="role-block__name">Mara Ellison</div>
    </div>
  </section>

  <section class="card card--back">
    <div class="contact">
      <div class="heading">Contact us</div>
      <div>018 274 9063</div>
      <div>hello@quillmoorhub.com.au</div>
      <div>www.quillmoorhub.com.au</div>
    </div>
    <div class="brand"><span class="brand__dot"></span><span class="brand__name">quillmoorhub</span></div>
    <div class="social">
      <div class="heading">Follow us on social</div>
      <div>friendsnet.com/user-name</div>
      <div>chirpline.com/user-name</div>
      <div>folioshare.com/user-name</div>
    </div>
    <div class="person">
      <div class="person__name">Mara Ellison</div>
      <div class="person__role">Founder</div>
    </div>
    <div class="back-blocks"><span class="c-light"></span><span class="c-grey"></span><span class="c-dark"></span></div>
    <div class="back-stripe"></div>
  </section>
</body>
</html>
```